Business Card Design

We are a manufacturing company that has been in business for over 30 years, established in 1981. We are looking to increase our business with defence force, government, and the major telecoms so the card needs to present the company as being cutting edge, secure, and professional.
Industry/Entity Type
Defence
Contact Information for Business Card
Name Gregory Pell
Phone 02 9374 5086
Fax 02 9453 7061
mobile 0427386204
Email Greg@Korvex.com.au
Webiste www.korvex.com.au
ABN 48 006 517 392
address: 17 Tallow Street Ingleburn NSW 2565
"Manufacturer of Antennas, GPS, Microwave, Cable Assemblies, RF, Military, & Telecommunications"

```html
<!DOCTYPE html>
<html lang="en">
<head>
<meta charset="utf-8">
<title>Korvex Business Card</title>
<link href="https://fonts.googleapis.com/css2?family=Fira+Sans:wght@300;400;500;600&family=Fira+Sans+Condensed:wght@600&display=swap" rel="stylesheet">
<style>
  :root {
    --navy: #0c1f4b;
    --rust: #b33a0a;
    --white: #ffffff;
    --backdrop: #e3e3e3;
  }
  * { margin: 0; padding: 0; box-sizing: border-box; }
  html, body { width: 1200px; height: 1200px; overflow: hidden; }
  body {
    background: var(--backdrop);
    font-family: "Fira Sans", Arial, sans-serif;
    position: relative;
  }
  .card { position: absolute; width: 607px; height: 370px; overflow: hidden; }

  /* Front */
  .card-front { left: 128px; top: 122px; background: var(--navy); color: var(--white); }
  .front-mark {
    position: absolute; left: 220px; top: 64px; width: 135px; height: 115px;
    background: var(--white);
  }
  .front-name {
    position: absolute; left: 0; width: 100%; top: 197px; text-align: center;
    font-weight: 600; font-size: 19px; letter-spacing: 3px; color: var(--white);
  }
  .tagline {
    position: absolute; left: 0; width: 100%; top: 259px; text-align: center;
    font-weight: 300; font-size: 17.5px; letter-spacing: 0.4px; line-height: 22px; color: var(--white);
  }

  /* Back */
  .card-back { left: 480px; top: 629px; background: var(--white); }
  .stripe { position: absolute; left: 0; width: 100%; height: 6px; background: var(--navy); }
  .stripe-1 { top: 0; } .stripe-2 { top: 12px; } .stripe-3 { top: 24px; }
  .footer-band { position: absolute; left: 0; bottom: 0; width: 100%; height: 29px; background: var(--rust); }
  .back-mark {
    position: absolute; left: 68px; top: 93px; width: 134px; height: 115px;
    background: var(--navy);
  }
  .back-name {
    position: absolute; left: 68px; width: 134px; top: 225px; text-align: center;
    font-weight: 600; font-size: 19px; letter-spacing: 3px; color: var(--rust);
  }
  .abn {
    position: absolute; left: 25px; width: 220px; top: 283px; text-align: center;
    font-weight: 300; font-size: 17.5px; letter-spacing: 0.2px; color: var(--navy);
  }
  .person { position: absolute; left: 345px; top: 76px; }
  .person-name {
    font-family: "Fira Sans Condensed", "Arial Narrow", sans-serif;
    font-weight: 600; font-size: 21px; letter-spacing: 0.4px; color: var(--rust); line-height: 22px;
  }
  .person-title { font-size: 14px; color: var(--navy); line-height: 18px; }
  .title-rule { position: absolute; left: 345px; right: 0; top: 119px; height: 6px; background: var(--navy); }

  .contacts { position: absolute; left: 343px; top: 136px; list-style: none; color: var(--navy); font-weight: 300; font-size: 17.5px; letter-spacing: 0.2px; }
  .contacts li { display: flex; align-items: flex-start; line-height: 21px; }
  .contacts svg { width: 14px; height: 14px; flex: none; margin: 4px 12px 0 0; }
  .contacts .gap { margin-top: 10px; }
  .contacts .gap-sm { margin-top: 8px; }
  .ico { fill: none; stroke: var(--rust); stroke-width: 1.8; }
  .ico-fill { fill: var(--rust); }
</style>
</head>
<body>

<section class="card card-front">
  <div class="front-mark"></div>
  <div class="front-name">KORVEX</div>
  <p class="tagline">Manufacturer of<br>Antennas, GPS, Microwave, Cable Assemblies,<br>RF, Military, &amp; Telecommunications"</p>
</section>

<section class="card card-back">
  <div class="stripe stripe-1"></div>
  <div class="stripe stripe-2"></div>
  <div class="stripe stripe-3"></div>

  <div class="back-mark"></div>
  <div class="back-name">KORVEX</div>
  <div class="abn">ABN 48 006 517 392</div>

  <div class="person">
    <div class="person-name">GREGORY PELL</div>
    <div class="person-title">Managing Director</div>
  </div>
  <div class="title-rule"></div>

  <ul class="contacts">
    <li>
      <svg viewBox="0 0 14 14"><path class="ico" d="M2 7 L7 2.5 L12 7 M3.5 6 V12 H10.5 V6 M6 12 V9 H8 V12"/></svg>
      <span>17 Tallow Street Arnvale<br>NSW 2591</span>
    </li>
    <li class="gap">
      <svg viewBox="0 0 14 14"><rect class="ico-fill" x="4" y="1.5" width="6" height="11" rx="1.5"/><rect x="5.5" y="3.5" width="3" height="3" fill="#fff"/></svg>
      <span>04 2738 6204</span>
    </li>
    <li>
      <svg viewBox="0 0 14 14"><path class="ico-fill" d="M3 1.5 L5.5 1.5 L6.5 4.5 L5 5.8 C5.8 7.6 6.6 8.6 8.2 9.2 L9.5 7.6 L12.5 8.6 L12.5 11 C12.5 12 11.6 12.6 10.6 12.5 C5.6 12 2 8.4 1.5 3.4 C1.4 2.4 2 1.5 3 1.5 Z"/></svg>
      <span>02 9374 5086</span>
    </li>
    <li>
      <svg viewBox="0 0 14 14"><path class="ico" d="M4 5 V1.5 H10 V5 M2 5 H12 V10 H2 Z M4 9 V12.5 H10 V9"/></svg>
      <span>02 9453 7061</span>
    </li>
    <li class="gap-sm">
      <svg viewBox="0 0 14 14"><path class="ico" d="M1.5 3 H12.5 V11 H1.5 Z M1.5 3 L7 8 L12.5 3"/></svg>
      <span>Greg@Korvex.com.au</span>
    </li>
    <li>
      <svg viewBox="0 0 14 14"><circle class="ico" cx="7" cy="7" r="5.5"/><path class="ico" d="M1.5 7 H12.5 M7 1.5 C4.5 4 4.5 10 7 12.5 M7 1.5 C9.5 4 9.5 10 7 12.5"/></svg>
      <span>www.korvex.com.au</span>
    </li>
  </ul>

  <div class="footer-band"></div>
</section>

</body>
</html>
```